Flyer for Choir Christmas Concert

Need colorful flyer for Christmas Choir Concert.

Requirements
Should not have
• I don't like musical symbols incorporated into the design.

```html
<!DOCTYPE html>
<html lang="en">
<head>
<meta charset="utf-8">
<title>Love and Joy – Cantoria Holiday Concert</title>
<link rel="stylesheet" href="https://fonts.googleapis.com/css2?family=Libre+Baskerville:ital@1&family=Playball&family=Lobster+Two:ital,wght@1,700&family=Roboto+Condensed:wght@400;700&family=Arimo:ital,wght@0,400;0,700;1,700&display=swap">
<style>
  :root {
    --plum: #4e2170;
    --plum-deep: #3f1a5c;
    --berry: #c2187a;
    --blush: #f6e4f0;
    --rose: #e59bcb;
    --scarlet: #e01e37;
    --ink: #1b1b1b;
    --paper: #ffffff;
  }
  * { margin: 0; padding: 0; box-sizing: border-box; }
  html, body { width: 927px; height: 1200px; overflow: hidden; background: var(--paper); }
  .flyer { position: relative; width: 927px; height: 1200px; overflow: hidden; font-family: "Roboto Condensed", sans-serif; color: var(--ink); }

  .masthead {
    position: absolute; left: 0; top: 0; width: 927px; height: 116px;
    background: var(--plum); color: var(--paper); text-align: center;
    font-family: "Libre Baskerville", serif; font-style: italic; font-size: 29px; line-height: 37px;
    padding-top: 22px;
  }

  .stage {
    position: absolute; left: 0; top: 116px; width: 927px; height: 819px;
    background:
      radial-gradient(ellipse at 78% 42%, rgba(255,255,255,0.55) 0%, rgba(255,255,255,0) 35%),
      linear-gradient(100deg, #ffffff 0%, #f8e6f2 30%, #eaa8d2 65%, #d14c9e 100%);
  }
  .ornaments {
    position: absolute; right: 0; top: 116px; width: 330px; height: 819px;
    background:
      radial-gradient(circle at 70% 14%, rgba(86,38,120,0.85) 0 48px, transparent 50px),
      radial-gradient(circle at 88% 37%, rgba(86,38,120,0.9) 0 75px, transparent 77px),
      radial-gradient(circle at 45% 70%, rgba(86,38,120,0.9) 0 80px, transparent 82px),
      radial-gradient(circle at 95% 88%, rgba(86,38,120,0.9) 0 78px, transparent 80px);
  }

  .presents { position: absolute; top: 186px; width: 927px; text-align: center; font-size: 30px; letter-spacing: 4px; }
  .title {
    position: absolute; top: 236px; left: 0; width: 927px; text-align: center;
    font-family: "Playball", cursive; font-size: 128px; line-height: 1; color: var(--scarlet);
    text-shadow: 0 2px 0 #fff;
  }
  .invitation {
    position: absolute; top: 420px; left: 0; width: 927px; text-align: center;
    font-family: "Lobster Two", cursive; font-style: italic; font-weight: 700; font-size: 30px; line-height: 40px;
  }

  .guests { position: absolute; left: 38px; top: 578px; }
  .guests .label { font-size: 23px; }
  .guests .ensemble { font-size: 34px; font-weight: 700; margin-top: 6px; }
  .guests .director { font-size: 23px; margin-top: 10px; }

  .schedule { position: absolute; left: 38px; top: 730px; }
  .schedule .date { font-size: 34px; font-weight: 700; line-height: 42px; }
  .schedule .venue { font-size: 24px; line-height: 42px; margin-top: 2px; }

  .footer-panel { position: absolute; left: 0; top: 935px; width: 927px; height: 218px; background: var(--paper); }
  .org-name {
    position: absolute; left: 26px; top: 960px;
    font-family: "Libre Baskerville", serif; font-size: 60px; color: var(--plum); letter-spacing: 1px;
  }
  .leadership { position: absolute; left: 40px; top: 1072px; font-family: "Arimo", sans-serif; font-size: 18px; line-height: 24px; }
  .leadership em { font-weight: 700; }

  .tickets { position: absolute; left: 560px; top: 955px; font-family: "Arimo", sans-serif; }
  .tickets .intro { font-size: 17px; }
  .tickets .price { font-size: 21px; font-weight: 700; line-height: 26px; display: flex; }
  .tickets .price span:first-child { width: 102px; }
  .tickets .price:first-of-type { margin-top: 6px; }
  .tickets .note { font-size: 16px; line-height: 20px; margin-top: 2px; width: 330px; }
  .tickets .web { font-size: 19px; font-weight: 700; margin-top: 8px; }

  .baseline {
    position: absolute; left: 0; top: 1153px; width: 927px; height: 47px;
    background: var(--plum-deep); color: var(--paper); text-align: center;
    font-size: 16px; line-height: 47px;
  }
</style>
</head>
<body>
<main class="flyer">
  <header class="masthead">
    <div>Cantoria: Voices of the High Desert</div>
    <div>Daniel Ashford, Artistic Director</div>
  </header>

  <section class="stage"></section>
  <div class="ornaments" role="img" aria-label="Hanging purple holiday ornaments with stars and snowflakes"></div>

  <div class="presents">Presents</div>
  <h1 class="title">Love and Joy</h1>
  <p class="invitation">Join the singers of Cantoria as we perform<br>carols, chorales, and other joyful and poignant<br>music of the season</p>

  <section class="guests">
    <div class="label">with special guests</div>
    <div class="ensemble">The Choirs of Juniper Middle School</div>
    <div class="director">Evan Marsh, Director</div>
  </section>

  <section class="schedule">
    <div class="date">Saturday, December 1 at 5:00pm</div>
    <div class="date">Sunday, December 2 at 3:00pm</div>
    <div class="venue">Grace Valley Community Church</div>
    <div class="venue">1480 Mesa Verde Avenue NE Albuquerque</div>
  </section>

  <section class="footer-panel"></section>
  <div class="org-name">Cantoria</div>
  <div class="leadership">
    <div>Daniel Ashford, <em>Artistic Director</em></div>
    <div>Rosa Delgado Quinn, <em>Executive Director</em></div>
  </div>

  <section class="tickets">
    <div class="intro">Tickets available online and at the door:</div>
    <div class="price"><span>General</span><span>$20</span></div>
    <div class="price"><span>Seniors</span><span>$15</span></div>
    <div class="price"><span>Students</span><span>$10</span></div>
    <div class="note">Complimentary childcare provided at both performances.</div>
    <div class="web">www.cantoria-abq.org</div>
  </section>

  <footer class="baseline">Cantoria is a 501(c)3 nonprofit organization, and an Ensemble-in-Residence at Grace Valley Community Church</footer>
</main>
</body>
</html>
```